Ember Lane Pet Supply

Thank you for your interest in this design contest. We are always welcome to questions and are looking forward to seeing what you can come up with.

We work on a Bootstrap platform with our custom built CMS. We require all designs to be sized accordingly with the bootstrap grid system found here: http://tilebasekit.com/css/#grid

At the start of a competition, we are looking for general Home Page Design concepts and an example product grid page.

Homepage: Slide Show/Featured Products/Specials

example website as a reference:https://www.brindlemoorgoods.com/

Store Product Grid: Show a grid of product thumbnails. Included elements are thumbnail and price. Also included are filters (sort by, show by grid/list).

No photos at this time but Logo is attached. Looking for good quality photo's around the web. Please read the attached creative brief in depth to get an idea f what the client is looking for. Thanks!

```html
<!DOCTYPE html>
<html lang="en">
<head>
<meta charset="utf-8">
<title>Ember Lane Pet Supply — Home</title>
<link rel="stylesheet" href="https://fonts.googleapis.com/css2?family=Montserrat:wght@400;600;700&family=Lato:wght@300;400;700&display=swap">
<style>
  :root {
    --backdrop: #1b1b1b;
    --white: #ffffff;
    --ink: #2e2e2e;
    --muted: #9a9a9a;
    --green: #6aa51d;
    --blue: #2aa7e0;
    --sand: #f4f0e3;
    --sand-border: #e6dfc9;
    --card-bar: #f1ead6;
    --line: #e3e3e3;
    --star-off: #d0d0d0;
  }
  * { box-sizing: border-box; margin: 0; padding: 0; }
  html, body { width: 831px; height: 1200px; overflow: hidden; background: var(--backdrop); }
  body { font-family: "Lato", Arial, sans-serif; color: var(--ink); }

  .page {
    position: absolute; left: 0; top: 41px;
    width: 522px; height: 702px;
    transform: scale(1.592); transform-origin: 0 0;
    background: var(--white); overflow: hidden;
  }
  .abs { position: absolute; }

  /* Header */
  .site-header { position: absolute; left: 0; top: 0; width: 522px; height: 49px; background: var(--white); box-shadow: 0 1px 2px rgba(0,0,0,.12); z-index: 2; }
  .brand { left: 57px; top: 14px; display: flex; align-items: center; gap: 4px; }
  .brand-mark { width: 9px; height: 9px; background: var(--green); }
  .brand-name { font-family: "Montserrat", sans-serif; font-weight: 700; font-size: 7px; color: var(--ink); line-height: 1.1; width: 52px; }
  .cart-summary { right: 57px; top: 7px; font-size: 5px; color: var(--green); display: flex; align-items: center; gap: 3px; }
  .main-nav { left: 134px; top: 28px; display: flex; gap: 0; font-family: "Montserrat", sans-serif; font-weight: 600; font-size: 6.2px; }
  .main-nav a { color: var(--ink); text-decoration: none; position: absolute; white-space: nowrap; }
  .main-nav a.login { color: var(--green); }

  /* Hero */
  .hero { left: 0; top: 49px; width: 522px; height: 220px;
    background:
      radial-gradient(ellipse at 62% 45%, #c9a274 0%, #b08a5e 22%, rgba(176,138,94,0) 45%),
      radial-gradient(ellipse at 28% 75%, #4a5d7a 0%, #3d4f6a 25%, rgba(61,79,106,0) 50%),
      linear-gradient(100deg, #8f7d6a 0%, #c9c2b8 35%, #e3ddd3 60%, #cbb79b 100%);
  }
  .hero-ring { position: absolute; left: 157px; top: 22px; width: 200px; height: 197px; border-radius: 50%; border: 1.5px solid rgba(255,255,255,.35); background: rgba(255,255,255,.08); }
  .hero-title { position: absolute; left: 229px; top: 137px; font-family: "Montserrat", sans-serif; font-weight: 700; font-size: 13px; color: var(--white); text-shadow: 0 1px 3px rgba(0,0,0,.35); }

  /* Section titles */
  .section-title { font-family: "Lato", sans-serif; font-weight: 400; font-size: 8.5px; color: #444; }

  /* Toolbar */
  .sort-box { left: 314px; top: 287px; width: 86px; height: 13px; border: 1px solid var(--line); font-size: 4.6px; color: var(--muted); display: flex; align-items: center; padding-left: 4px; }
  .sort-box b { color: var(--ink); font-weight: 400; margin-left: 2px; }
  .sort-box .caret { position: absolute; right: 0; top: 0; width: 10px; height: 11px; border-left: 1px solid var(--line); display: flex; align-items: center; justify-content: center; }
  .view-label { left: 407px; top: 290px; font-size: 4.6px; color: var(--muted); }
  .view-btn { top: 287px; width: 12px; height: 12px; border: 1px solid var(--line); display: flex; align-items: center; justify-content: center; }
  .view-btn.active { background: var(--blue); border-color: var(--blue); }

  /* Product cards */
  .product-card { top: 308px; width: 96px; height: 139px; }
  .product-thumb { position: absolute; left: 0; top: 0; width: 96px; height: 66px; border: 1px solid var(--line); }
  .product-body { position: absolute; left: 0; top: 66px; width: 96px; height: 58px; border: 1px solid var(--line); border-top: 0; }
  .product-name { position: absolute; left: 5px; top: 5px; font-size: 5.3px; font-weight: 700; color: var(--ink); }
  .product-by { position: absolute; left: 5px; top: 14px; font-size: 4.4px; color: var(--muted); }
  .product-price { position: absolute; left: 5px; top: 22px; font-family: "Montserrat", sans-serif; font-weight: 700; font-size: 7.4px; color: var(--green); }
  .product-rule { position: absolute; left: 5px; right: 5px; top: 35px; border-top: 1px solid var(--line); }
  .product-stars { position: absolute; left: 5px; top: 42px; display: flex; gap: 0.6px; }
  .product-reviews { position: absolute; right: 5px; top: 42px; font-size: 4.2px; color: var(--muted); }
  .product-actions { position: absolute; left: 0; top: 124px; width: 96px; height: 15px; background: var(--card-bar); font-size: 4.2px; color: var(--ink); }
  .product-actions span { position: absolute; top: 5px; display: flex; align-items: center; gap: 2px; }

  .slider-arrow { width: 11px; height: 11px; border-radius: 50%; background: #d4d0c4; display: flex; align-items: center; justify-content: center; }

  /* Specials */
  .specials { left: 0; top: 466px; width: 522px; height: 110px; background: var(--sand); }
  .special-box { top: 38px; width: 130px; height: 46px; background: var(--white); border: 3px solid var(--sand-border); display: flex; align-items: center; padding-left: 8px; gap: 7px; }
  .special-title { font-family: "Montserrat", sans-serif; font-weight: 600; font-size: 8.3px; color: var(--green); line-height: 1; }
  .special-sub { font-size: 4.6px; color: var(--muted); margin-top: 2px; }

  /* News + Events */
  .news-photo { left: 57px; top: 615px; width: 199px; height: 81px;
    background: linear-gradient(90deg, #6e3a1d 0%, #a4572a 35%, #c77a3e 55%, #4f7fb3 75%, #c9883f 100%); }
  .event { left: 265px; width: 210px; height: 26px; }
  .event-date { position: absolute; left: 0; top: 0; width: 24px; height: 24px; background: var(--green); color: var(--white); text-align: center; font-family: "Montserrat", sans-serif; line-height: 1; }
  .event-date .day { display: block; font-size: 9px; font-weight: 700; margin-top: 3px; }
  .event-date .month { display: block; font-size: 5.2px; margin-top: 1px; }
  .event-text { position: absolute; left: 29px; top: 1px; width: 172px; font-family: "Montserrat", sans-serif; font-weight: 600; font-size: 6.3px; line-height: 1.45; color: var(--ink); }
</style>
</head>
<body>
<div class="page">

  <header class="site-header">
    <div class="abs brand"><span class="brand-mark"></span><span class="brand-name">Ember Lane Pet Supply</span></div>
    <div class="abs cart-summary">
      <svg width="7" height="6" viewBox="0 0 14 12"><path d="M0 1h3l2 7h7l2-5H4" fill="none" stroke="#6aa51d" stroke-width="1.6"/><circle cx="6" cy="10.5" r="1.2" fill="#6aa51d"/><circle cx="11" cy="10.5" r="1.2" fill="#6aa51d"/></svg>
      <span>( 03 ) Items - $12,560</span>
    </div>
    <nav class="abs main-nav">
      <a style="left:0">Dogs</a>
      <a style="left:34px">Cats</a>
      <a style="left:64px">Our Story</a>
      <a style="left:113px">The Scoop</a>
      <a style="left:165px">Find a Retailer</a>
      <a style="left:231px">Become a Partner</a>
      <a class="login" style="left:310px">Login</a>
    </nav>
  </header>

  <section class="abs hero" role="img" aria-label="Slideshow photo: a person on a sofa playing with a shaggy tan dog holding an orange ball">
    <div class="hero-ring"></div>
    <h1 class="hero-title">We Know Their Needs</h1>
  </section>

  <h2 class="abs section-title" style="left:57px;top:281px">Featured Products</h2>
  <div class="abs sort-box">Sort by:<b>Default Sorting</b>
    <span class="caret"><svg width="4" height="3" viewBox="0 0 8 5"><path d="M0 0l4 5 4-5" fill="none" stroke="#777" stroke-width="1.2"/></svg></span>
  </div>
  <div class="abs view-label">View as:</div>
  <div class="abs view-btn" style="left:435px">
    <svg width="5" height="5" viewBox="0 0 10 10" fill="#aaa"><rect x="0" y="0" width="2" height="2"/><rect x="3" y="0" width="7" height="2"/><rect x="0" y="4" width="2" height="2"/><rect x="3" y="4" width="7" height="2"/><rect x="0" y="8" width="2" height="2"/><rect x="3" y="8" width="7" height="2"/></svg>
  </div>
  <div class="abs view-btn active" style="left:452px">
    <svg width="5" height="5" viewBox="0 0 10 10" fill="#fff"><rect x="0" y="0" width="4" height="4"/><rect x="6" y="0" width="4" height="4"/><rect x="0" y="6" width="4" height="4"/><rect x="6" y="6" width="4" height="4"/></svg>
  </div>

  <div class="abs slider-arrow" style="left:37px;top:363px"><svg width="4" height="5" viewBox="0 0 6 8"><path d="M5 0L1 4l4 4" fill="none" stroke="#fff" stroke-width="1.6"/></svg></div>
  <div class="abs slider-arrow" style="left:470px;top:363px"><svg width="4" height="5" viewBox="0 0 6 8"><path d="M1 0l4 4-4 4" fill="none" stroke="#fff" stroke-width="1.6"/></svg></div>

  <!-- product cards -->
  <article class="abs product-card" style="left:57px">
    <div class="product-thumb" role="img" aria-label="Product photo: patterned dog collar and leash" style="background:radial-gradient(ellipse at 50% 50%,#d9b8c7 0%,#9ecbd9 30%,#fff 60%)"></div>
    <div class="product-body">
      <div class="product-name">Aliquam suscipit</div><div class="product-by">By Maren Holt</div>
      <div class="product-price">$589.50</div><div class="product-rule"></div>
      <div class="product-stars"><svg width="28" height="5" viewBox="0 0 56 10"><g fill="#6aa51d"><path id="st" d="M5 0l1.5 3.2 3.5.4-2.6 2.4.7 3.5L5 7.8 1.9 9.5l.7-3.5L0 3.6l3.5-.4z"/><use href="#st" x="11"/><use href="#st" x="22"/><use href="#st" x="33"/></g><use href="#st" x="44" fill="#d0d0d0"/></svg></div>
      <div class="product-reviews">14 reviews</div>
    </div>
    <div class="product-actions"><span style="left:5px"><svg width="5" height="4" viewBox="0 0 10 8"><path d="M0 0h2l1 5h6l1-4H2.5" fill="#2e2e2e"/></svg>Add to cart</span><span style="left:63px"><svg width="4" height="4" viewBox="0 0 8 8"><circle cx="4" cy="4" r="4" fill="#2e2e2e"/><rect x="3.4" y="3.4" width="1.2" height="3" fill="#fff"/><rect x="3.4" y="1.4" width="1.2" height="1.2" fill="#fff"/></svg>Details</span></div>
  </article>

  <article class="abs product-card" style="left:161px">
    <div class="product-thumb" role="img" aria-label="Product photo: grey sofa-style dog bed with a small dog" style="background:radial-gradient(ellipse at 50% 55%,#4a4a4a 0%,#6a6a6a 28%,#fff 55%)"></div>
    <div class="product-body">
      <div class="product-name">Aliquam suscipit</div><div class="product-by">By Maren Holt</div>
      <div class="product-price">$589.50</div><div class="product-rule"></div>
      <div class="product-stars"><svg width="28" height="5" viewBox="0 0 56 10"><g fill="#6aa51d"><use href="#st"/><use href="#st" x="11"/><use href="#st" x="22"/><use href="#st" x="33"/></g><use href="#st" x="44" fill="#d0d0d0"/></svg></div>
      <div class="product-reviews">14 reviews</div>
    </div>
    <div class="product-actions"><span style="left:5px"><svg width="5" height="4" viewBox="0 0 10 8"><path d="M0 0h2l1 5h6l1-4H2.5" fill="#2e2e2e"/></svg>Add to cart</span><span style="left:63px"><svg width="4" height="4" viewBox="0 0 8 8"><circle cx="4" cy="4" r="4" fill="#2e2e2e"/><rect x="3.4" y="3.4" width="1.2" height="3" fill="#fff"/><rect x="3.4" y="1.4" width="1.2" height="1.2" fill="#fff"/></svg>Details</span></div>
  </article>

  <article class="abs product-card" style="left:265px">
    <div class="product-thumb" role="img" aria-label="Product photo: bag of dry dog food" style="background:radial-gradient(ellipse 30% 50% at 50% 50%,#d9c9a0 0%,#c0432e 45%,#fff 100%)"></div>
    <div class="product-body">
      <div class="product-name">Aliquam suscipit</div><div class="product-by">By Maren Holt</div>
      <div class="product-price">$589.50</div><div class="product-rule"></div>
      <div class="product-stars"><svg width="28" height="5" viewBox="0 0 56 10"><g fill="#6aa51d"><use href="#st"/><use href="#st" x="11"/><use href="#st" x="22"/><use href="#st" x="33"/></g><use href="#st" x="44" fill="#d0d0d0"/></svg></div>
      <div class="product-reviews">14 reviews</div>
    </div>
    <div class="product-actions"><span style="left:5px"><svg width="5" height="4" viewBox="0 0 10 8"><path d="M0 0h2l1 5h6l1-4H2.5" fill="#2e2e2e"/></svg>Add to cart</span><span style="left:63px"><svg width="4" height="4" viewBox="0 0 8 8"><circle cx="4" cy="4" r="4" fill="#2e2e2e"/><rect x="3.4" y="3.4" width="1.2" height="3" fill="#fff"/><rect x="3.4" y="1.4" width="1.2" height="1.2" fill="#fff"/></svg>Details</span></div>
  </article>

  <article class="abs product-card" style="left:369px">
    <div class="product-thumb" role="img" aria-label="Product photo: round brown plush pet bed" style="background:radial-gradient(ellipse 42% 32% at 50% 55%,#c7b08e 0%,#6b4a32 55%,#fff 100%)"></div>
    <div class="product-body">
      <div class="product-name">Aliquam suscipit</div><div class="product-by">By Maren Holt</div>
      <div class="product-price">$589.50</div><div class="product-rule"></div>
      <div class="product-stars"><svg width="28" height="5" viewBox="0 0 56 10"><g fill="#6aa51d"><use href="#st"/><use href="#st" x="11"/><use href="#st" x="22"/><use href="#st" x="33"/></g><use href="#st" x="44" fill="#d0d0d0"/></svg></div>
      <div class="product-reviews">14 reviews</div>
    </div>
    <div class="product-actions"><span style="left:5px"><svg width="5" height="4" viewBox="0 0 10 8"><path d="M0 0h2l1 5h6l1-4H2.5" fill="#2e2e2e"/></svg>Add to cart</span><span style="left:63px"><svg width="4" height="4" viewBox="0 0 8 8"><circle cx="4" cy="4" r="4" fill="#2e2e2e"/><rect x="3.4" y="3.4" width="1.2" height="3" fill="#fff"/><rect x="3.4" y="1.4" width="1.2" height="1.2" fill="#fff"/></svg>Details</span></div>
  </article>

  <!-- Specials -->
  <section class="abs specials">
    <h2 class="abs section-title" style="left:57px;top:11px">Specials</h2>
    <div class="abs special-box" style="left:57px">
      <svg width="16" height="16" viewBox="0 0 20 20"><path d="M8 3L2 9l6 6v-4c5 0 8 1 10 6 0-7-4-10-10-10z" fill="#6aa51d"/></svg>
      <div><div class="special-title">Free Return</div><div class="special-sub">Free Return for 100 days</div></div>
    </div>
    <div class="abs special-box" style="left:196px">
      <svg width="18" height="14" viewBox="0 0 24 18"><path d="M0 2h14v10H0zM14 5h5l4 4v3h-9z" fill="#6aa51d"/><circle cx="5" cy="14" r="2.6" fill="#6aa51d" stroke="#fff"/><circle cx="18" cy="14" r="2.6" fill="#6aa51d" stroke="#fff"/></svg>
      <div><div class="special-title">Free Shipping</div><div class="special-sub">Only for Our Special Offers</div></div>
    </div>
    <div class="abs special-box" style="left:334px">
      <svg width="17" height="17" viewBox="0 0 20 20"><path d="M10 0l2.2 2.6 3.3-.9.6 3.4 3.3 1-1.4 3.1 1.9 2.8-3 1.6.1 3.4-3.4-.2-1.6 3-2.8-1.9L6 19.9l-1-3.3-3.4-.6.9-3.3L0 10.6l2.6-2.2-.9-3.3 3.4-.6 1-3.3 3.1 1.4z" fill="#6aa51d"/><text x="10" y="13.5" text-anchor="middle" font-family="Montserrat, sans-serif" font-weight="700" font-size="10" fill="#fff">%</text></svg>
      <div><div class="special-title">% Discount</div><div class="special-sub">For Over $120</div></div>
    </div>
  </section>

  <!-- News + Events -->
  <h2 class="abs section-title" style="left:57px;top:591px">Latest News</h2>
  <div class="abs news-photo" role="img" aria-label="News photo: a child lying on a wooden deck beside a spaniel among autumn leaves"></div>

  <h2 class="abs section-title" style="left:264px;top:591px">Event Calendar</h2>
  <div class="abs event" style="top:616px">
    <div class="event-date"><span class="day">20</span><span class="month">May</span></div>
    <p class="event-text">Lorem ipsum dolor sit amet, consectetuer adicing elit, sed diam nonummy nibh</p>
  </div>
  <div class="abs event" style="top:650px">
    <div class="event-date"><span class="day">20</span><span class="month">May</span></div>
    <p class="event-text">Maecenas tempus, tellus eget condimen tum rhoncus, sem quam semper libero</p>
  </div>
  <div class="abs event" style="top:684px">
    <div class="event-date"><span class="day">20</span><span class="month">May</span></div>
    <p class="event-text">Curabitur ligula sapien, tincidunt non, euismod vitae, posuere imperdiet</p>
  </div>

</div>
</body>
</html>
```